Powerpoint template & style design project

KMaldrey Consulting is an IT technology firm specializing in mobility and telecommunications applications. We provide technical consulting to global companies that want to build mobile applications and take critical business applications and move them into the cloud.
We would like to see designs that use the color blue. The final design should communicate confidence, agility and speak to technology focused customers. Forward progress and/or motion should be conveyed.

Target Market(s)

Government customers and large enterprise companies

Industry/Entity Type

Telecommunications

Font styles to use
Sans Serif

Colors
0555a3

Requirements
Must have
• different slides: Cover page, title slide, main content, transition slide, close out slide..

```html
<!DOCTYPE html>
<html lang="en">
<head>
<meta charset="utf-8">
<title>KMaldrey Consulting – Slide Template</title>
<link href="https://fonts.googleapis.com/css2?family=Arimo:wght@400;700&family=Carlito:wght@400;700&display=swap" rel="stylesheet">
<style>
  :root {
    --brand-blue: #0555a3;
    --accent-blue: #1565c0;
    --chart-blue: #4a7ebb;
    --chart-grey: #878787;
    --marker-red: #e0301e;
    --ink: #111111;
    --body-ink: #333333;
    --rule: #7a7a7a;
    --backdrop: #78797b;
    --paper: #ffffff;
    --photo-tone: linear-gradient(160deg, #d9d9d9 0%, #8c8c8c 60%, #3a3a3a 100%);
  }
  * { margin: 0; padding: 0; box-sizing: border-box; }
  html, body { width: 924px; height: 1200px; overflow: hidden; }
  body { background: var(--backdrop); position: relative; font-family: "Carlito", "Calibri", sans-serif; }

  .slide { position: absolute; background: var(--paper); overflow: hidden; }
  .slide--team { left: 80px; top: 26px; width: 731px; height: 548px; }
  .slide--chart { left: 73px; top: 601px; width: 748px; height: 560px; }

  .slide-number {
    position: absolute; left: 0; top: 49px; width: 43px; height: 73px;
    background: var(--brand-blue); color: var(--paper);
    font: 400 16px "Arimo", Arial, sans-serif;
    display: flex; align-items: center; justify-content: center;
  }
  .slide-title {
    position: absolute; left: 81px; top: 74px; white-space: nowrap;
    font: 400 29px/1 "Arimo", Arial, sans-serif; color: var(--ink); letter-spacing: 0.2px;
  }
  .slide-title .highlight { color: var(--accent-blue); }

  .member { position: absolute; top: 139px; width: 140px; margin-left: -70px; text-align: center; }
  .member__photo {
    width: 122px; height: 122px; margin: 0 auto; border-radius: 50%;
    border: 1.5px solid var(--accent-blue); padding: 4px;
  }
  .member__photo span { display: block; width: 100%; height: 100%; border-radius: 50%; background: var(--photo-tone); }
  .member__name { margin-top: 10px; font: 700 20px/1 "Arimo", Arial, sans-serif; color: var(--accent-blue); }
  .member__role { margin-top: 6px; font: 400 15px/1 "Arimo", Arial, sans-serif; color: var(--ink); }
  .member__bio { margin-top: 5px; font-size: 12.5px; line-height: 16px; color: var(--body-ink); }

  .footer-brand {
    position: absolute; left: 22px; display: flex; align-items: center; gap: 7px;
    font: 400 16px/1 "Carlito", "Calibri", sans-serif; color: var(--ink); white-space: nowrap;
  }
  .footer-brand__dot { width: 9px; height: 9px; background: var(--brand-blue); }
  .footer-rule { position: absolute; height: 1px; background: var(--rule); }
  .slide--team .footer-brand { top: 508px; }
  .slide--team .footer-rule { left: 177px; width: 525px; top: 517px; }
  .slide--chart .footer-brand { top: 519px; }
  .slide--chart .footer-rule { left: 181px; width: 536px; top: 528px; }

  .bar-chart { position: absolute; left: 0; top: 0; }
  .bar-chart text { font-family: "Carlito", "Calibri", sans-serif; fill: var(--ink); }

  .note { position: absolute; left: 444px; width: 260px; }
  .note__marker { position: absolute; left: 0; top: 0; width: 14px; height: 14px; border-radius: 2px; }
  .note__marker--blue { background: var(--accent-blue); }
  .note__marker--red { background: var(--marker-red); }
  .note__heading { position: absolute; left: 32px; top: -2px; font: 700 17px/1 "Carlito", "Calibri", sans-serif; color: var(--ink); white-space: nowrap; }
  .note__text { position: absolute; left: 28px; top: 28px; font-size: 13px; line-height: 18.5px; color: var(--body-ink); white-space: nowrap; }
  .note--first { top: 144px; }
  .note--second { top: 288px; }
</style>
</head>
<body>

<section class="slide slide--team">
  <div class="slide-number">02</div>
  <h1 class="slide-title">YOUR MAIN TITLE <span class="highlight">SLIDE COMES HERE</span></h1>

  <article class="member" style="left:135px">
    <div class="member__photo"><span role="img" aria-label="Portrait photo of team member"></span></div>
    <h2 class="member__name">JOHN DOE</h2>
    <p class="member__role">Manager</p>
    <p class="member__bio">Corporate network<br>So they can quickly<br>Identify and address<br>Suspicious activity<br>On the network<br>That could lead to</p>
  </article>
  <article class="member" style="left:279px">
    <div class="member__photo"><span role="img" aria-label="Portrait photo of team member"></span></div>
    <h2 class="member__name">JOHN DOE</h2>
    <p class="member__role">Manager</p>
    <p class="member__bio">Corporate network<br>So they can quickly<br>Identify and address<br>Suspicious activity<br>On the network<br>That could lead to</p>
  </article>
  <article class="member" style="left:422px">
    <div class="member__photo"><span role="img" aria-label="Portrait photo of team member"></span></div>
    <h2 class="member__name">JOHN DOE</h2>
    <p class="member__role">Manager</p>
    <p class="member__bio">Corporate network<br>So they can quickly<br>Identify and address<br>Suspicious activity<br>On the network<br>That could lead to</p>
  </article>
  <article class="member" style="left:564px">
    <div class="member__photo"><span role="img" aria-label="Portrait photo of team member"></span></div>
    <h2 class="member__name">JOHN DOE</h2>
    <p class="member__role">Manager</p>
    <p class="member__bio">Corporate network<br>So they can quickly<br>Identify and address<br>Suspicious activity<br>On the network<br>That could lead to</p>
  </article>

  <div class="footer-brand"><span class="footer-brand__dot"></span>KMaldrey Consulting</div>
  <div class="footer-rule"></div>
</section>

<section class="slide slide--chart">
  <div class="slide-number">02</div>
  <h1 class="slide-title">YOUR CHART <span class="highlight">SLIDE COMES HERE</span></h1>

  <svg class="bar-chart" width="440" height="410" viewBox="0 0 440 410" role="img" aria-label="Bar chart of two series across four categories">
    <g stroke="#c8c8c8" stroke-width="1">
      <line x1="79" y1="190" x2="315" y2="190"/>
      <line x1="79" y1="225" x2="315" y2="225"/>
      <line x1="79" y1="259" x2="315" y2="259"/>
      <line x1="79" y1="294" x2="315" y2="294"/>
      <line x1="79" y1="328" x2="315" y2="328"/>
    </g>
    <line x1="79" y1="363" x2="315" y2="363" stroke="#8a8a8a"/>
    <line x1="79" y1="190" x2="79" y2="363" stroke="#8a8a8a"/>
    <g font-size="16" text-anchor="middle">
      <text x="65" y="196">5</text><text x="65" y="231">4</text><text x="65" y="265">3</text>
      <text x="65" y="300">2</text><text x="65" y="334">1</text><text x="65" y="369">0</text>
    </g>
    <g fill="var(--chart-blue)">
      <rect x="91" y="214" width="13" height="149"/>
      <rect x="150" y="277" width="13" height="86"/>
      <rect x="209" y="242" width="13" height="121"/>
      <rect x="267" y="207" width="13" height="156"/>
    </g>
    <g fill="var(--chart-grey)">
      <rect x="104" y="280" width="13" height="83"/>
      <rect x="163" y="211" width="13" height="152"/>
      <rect x="222" y="301" width="13" height="62"/>
      <rect x="280" y="266" width="13" height="97"/>
    </g>
    <g font-size="11.5" text-anchor="middle">
      <text x="124" y="387">Category 1</text><text x="183" y="387">Category 2</text>
      <text x="241" y="387">Category 3</text><text x="299" y="387">Category 4</text>
    </g>
    <rect x="334" y="272" width="6" height="6" fill="var(--chart-blue)"/>
    <text x="343" y="279" font-size="11">Series 1</text>
    <rect x="334" y="293" width="6" height="6" fill="var(--chart-grey)"/>
    <text x="343" y="300" font-size="11">Series 2</text>
  </svg>

  <div class="note note--first">
    <span class="note__marker note__marker--blue"></span>
    <h3 class="note__heading">Good or service:</h3>
    <p class="note__text">&nbsp;that is new or significantly<br>improved. This includes significant<br>improvements in technical</p>
  </div>
  <div class="note note--second">
    <span class="note__marker note__marker--red"></span>
    <h3 class="note__heading">Good or service:</h3>
    <p class="note__text">&nbsp;that is new or significantly<br>improved. This includes significant<br>improvements in technical</p>
  </div>

  <div class="footer-brand"><span class="footer-brand__dot"></span>KMaldrey Consulting</div>
  <div class="footer-rule"></div>
</section>

</body>
</html>
```